Coach company requires modern brochure

We need a brochure designed that shows our various coach services. The aim of the brochure is to attract new business, therefore we need something that is modern, eye-catching and uses a lot of imagery/design rather than being text heavy.

I have all the images that can be sent via dropbox or google drive if you want to request them.

Target Market(s)

Wedding planners, event companies, school business managers, sporting groups

Industry/Entity Type

Tourism

Requirements
Must have
• 4 x a4 pages
• Bold and eye catching cover page

```html
<!DOCTYPE html>
<html lang="en">
<head>
<meta charset="utf-8">
<title>Ridgeway Shore Transport – Brochure</title>
<link rel="stylesheet" href="https://fonts.googleapis.com/css2?family=Questrial&family=Open+Sans:wght@400;700&family=Parisienne&display=swap">
<style>
  :root{
    --green:#3a9f40;
    --green-dark:#2a8a35;
    --green-light:#8cc63f;
    --blue:#3ba3dc;
    --blue-light:#a9d8f1;
    --blue-pale:#e4f3fb;
    --teal:#2a8fc1;
    --orange:#f07b2a;
    --ink:#5a5a5a;
    --white:#ffffff;
    --stage:#e4e4e4;
  }
  *{box-sizing:border-box;margin:0;padding:0}
  html,body{width:1049px;height:1200px;overflow:hidden}
  body{background:var(--stage);font-family:"Open Sans",Arial,sans-serif;color:var(--ink)}

  .spread{position:absolute;left:44px;width:960px;height:340px;display:flex;box-shadow:0 10px 24px rgba(0,0,0,.18)}
  .spread--cover{top:110px}
  .spread--inside{top:660px}
  .page{position:relative;width:480px;height:340px;overflow:hidden;background:var(--white)}
  .page svg.bg{position:absolute;inset:0;width:100%;height:100%}

  .photo{position:absolute;border-radius:50%;border:4px solid var(--white);box-shadow:0 2px 6px rgba(0,0,0,.25)}
  .photo--stadium{background:radial-gradient(circle at 50% 70%,#3f8f3a,#6aa84f 45%,#7b8a99 70%,#b9c3cc)}
  .photo--beach{background:linear-gradient(#cfd9e2 0%,#aebfcc 45%,#5c6b52 55%,#c9b89a 80%)}
  .photo--coach-interior{background:radial-gradient(circle at 40% 40%,#dfe6ec,#8fa2b3 60%,#3c4c5c)}
  .photo--seats{background:radial-gradient(circle at 60% 50%,#c4ced8,#6f8496 55%,#2d3a46)}
  .photo--venue{background:radial-gradient(circle at 50% 50%,#eef3f1,#c7d8d3 60%,#8fa9a4)}
  .photo--garden{background:radial-gradient(circle at 50% 40%,#8fb06b,#4e7a3a 55%,#2f4a2a)}
  .photo--students{background:linear-gradient(#9fc3e0 0%,#7fa6c7 40%,#5d8bb8 65%,#4d6e3c)}
  .photo--pool{background:radial-gradient(circle at 50% 50%,#6fd0e8,#2aa6cf 60%,#157a9c)}
  .photo--field{background:radial-gradient(circle at 50% 70%,#3d9a3a,#5fae4c 45%,#8a98a6 70%,#c2ccd4)}
  .photo--coach{position:absolute;border-radius:0;border:none;box-shadow:none;
    background:linear-gradient(100deg,#d9e4ec 0%,#f4f7f9 40%,#c8d3dc 70%,#7d8f6a 100%)}

  /* back cover */
  .back{background:linear-gradient(120deg,var(--green-dark),var(--green) 60%,#46ad48)}
  .brand{position:absolute;font-family:"Questrial",Arial,sans-serif;white-space:nowrap;display:flex;align-items:center;gap:7px}
  .brand__dot{width:14px;height:14px;border-radius:50%}
  .brand--back{left:95px;top:108px;color:#cbe6c4;font-size:21px}
  .brand--back .brand__dot{background:#cbe6c4}
  .stamp{position:absolute;left:272px;top:24px;width:64px;height:64px;border-radius:50%;border:2px solid var(--white);transform:rotate(-12deg)}
  .contact{position:absolute;left:150px;top:150px;width:160px;text-align:center;color:var(--white)}
  .contact__title{font-weight:700;font-size:9px}
  .contact__phone{font-size:13px;margin:3px 0 2px}
  .contact__line{font-size:7px;line-height:11px}
  .social{position:absolute;left:170px;top:220px;color:var(--white);font-size:7px;line-height:14px}
  .social li{list-style:none;display:flex;align-items:center;gap:5px}
  .social__icon{width:8px;height:8px;border-radius:50%;background:var(--white)}

  /* front cover */
  .brand--front{left:28px;top:26px;color:var(--teal);font-size:16px}
  .brand--front .brand__dot{background:var(--teal)}
  .tagline{position:absolute;left:300px;top:232px;font-family:"Parisienne",cursive;color:var(--white);font-size:24px;line-height:24px;text-shadow:0 1px 3px rgba(0,0,0,.35)}
  .tagline span{display:block;padding-left:26px}
  .front-url{position:absolute;left:40px;top:318px;font-size:7px;color:var(--teal)}

  /* inside */
  .section{position:absolute;font-size:6.4px;line-height:8.6px}
  .section h2{font-size:10px;font-weight:700;color:var(--green);margin-bottom:3px}
  .section--on-blue{color:var(--white)}
  .section--on-blue h2{color:var(--white)}
  .note{position:absolute;border:1px solid var(--orange);background:var(--white);color:var(--orange);font-size:6.4px;line-height:8.6px;padding:5px 6px}
  .note strong{display:block;color:var(--green);margin-top:3px}
  .closing{position:absolute;right:40px;bottom:14px;width:130px;font-size:6.4px;line-height:8.6px}
  .closing strong{color:var(--teal)}
</style>
</head>
<body>

<!-- Outside spread: back cover + front cover -->
<section class="spread spread--cover">
  <article class="page back">
    <svg class="bg" viewBox="0 0 480 340" preserveAspectRatio="none" aria-hidden="true">
      <path d="M0 0 H44 C20 80 70 170 36 240 C20 280 30 320 40 340 H0 Z" fill="var(--blue-light)"/>
      <path d="M0 0 H28 C6 90 52 170 20 250 C10 290 18 320 26 340 H0 Z" fill="var(--green-light)" opacity=".85"/>
      <path d="M0 0 H12 C-4 100 30 180 6 260 L0 340 Z" fill="var(--blue)"/>
      <path d="M44 0 C20 80 70 170 36 240 C20 280 30 320 40 340" fill="none" stroke="var(--white)" stroke-width="2" opacity=".7"/>
    </svg>
    <div class="brand brand--back"><span class="brand__dot"></span>Ridgeway Shore Transport</div>
    <div class="stamp" role="img" aria-label="Welcome badge"></div>
    <div class="contact">
      <p class="contact__title">Contact Us</p>
      <p class="contact__phone">1300 000 482</p>
      <p class="contact__line">info@ridgewayshore.com</p>
      <p class="contact__line">www.ridgewayshore.com</p>
    </div>
    <ul class="social">
      <li><span class="social__icon"></span>/RidgewayShoreCoaches</li>
      <li><span class="social__icon"></span>@ridgewayshore_coaches</li>
    </ul>
  </article>

  <article class="page front">
    <svg class="bg" viewBox="0 0 480 340" preserveAspectRatio="none" aria-hidden="true">
      <defs>
        <linearGradient id="frontSky" x1="0" y1="0" x2="0" y2="1">
          <stop offset="0" stop-color="#ffffff"/><stop offset="1" stop-color="var(--blue-pale)"/>
        </linearGradient>
      </defs>
      <rect width="480" height="340" fill="url(#frontSky)"/>
      <path d="M0 96 C120 60 200 80 300 50 C380 26 440 20 480 14 V30 C430 36 380 44 300 70 C200 100 120 84 0 112 Z" fill="var(--green)"/>
      <path d="M0 112 C120 84 200 100 300 70 C380 44 430 36 480 30 V40 C430 48 380 58 300 84 C200 114 120 98 0 124 Z" fill="var(--blue-light)"/>
      <path d="M0 250 C100 290 200 300 300 270 C380 246 440 250 480 262 V340 H0 Z" fill="var(--blue-light)"/>
      <path d="M0 268 C110 305 210 312 310 286 C390 264 440 268 480 278 V340 H0 Z" fill="var(--blue)"/>
      <path d="M0 284 C110 318 220 322 320 300 C400 282 440 286 480 294 V340 H0 Z" fill="var(--white)"/>
    </svg>
    <div class="photo--coach" style="left:170px;top:48px;width:310px;height:232px;clip-path:path('M0 32 C80 18 160 4 310 0 V232 C230 222 150 232 0 242 Z')" role="img" aria-label="Photo of a white coach parked in front of trees"></div>
    <div class="brand brand--front"><span class="brand__dot"></span>Ridgeway Shore Transport</div>
    <div class="photo photo--stadium" style="left:12px;top:80px;width:112px;height:112px" role="img" aria-label="Photo of a sports stadium with green field"></div>
    <div class="photo photo--beach" style="left:100px;top:140px;width:100px;height:100px" role="img" aria-label="Photo of a beach with a tree on the shore"></div>
    <p class="tagline">Connecting<span>the Coast....</span></p>
    <p class="front-url">www.ridgewayshore.com</p>
  </article>
</section>

<!-- Inside spread -->
<section class="spread spread--inside">
  <article class="page inside-left">
    <svg class="bg" viewBox="0 0 480 340" preserveAspectRatio="none" aria-hidden="true">
      <path d="M0 0 H150 C190 60 150 120 190 170 C220 210 300 200 360 250 C400 285 440 310 480 330 V340 H0 Z" fill="var(--blue-pale)"/>
      <path d="M0 0 H140 C175 50 130 120 120 180 C110 230 60 240 0 250 Z" fill="var(--blue)"/>
      <path d="M140 0 C175 50 130 120 120 180 C110 230 60 240 0 250" fill="none" stroke="var(--green-light)" stroke-width="5"/>
      <path d="M150 0 C185 50 140 122 130 184 C120 236 64 248 0 260" fill="none" stroke="var(--green)" stroke-width="2"/>
      <path d="M200 340 C260 300 330 300 380 320 C420 336 450 338 480 334 V340 Z" fill="var(--blue-light)"/>
    </svg>
    <div class="section section--on-blue" style="left:14px;top:14px;width:116px">
      <h2>About Us</h2>
      <p>We are a family run coach company serving the coast and hinterland with modern, comfortable vehicles and friendly, experienced drivers. Whatever the group size, we plan every trip with care so you can relax and enjoy the journey.</p>
    </div>
    <div class="photo photo--coach-interior" style="left:-6px;top:240px;width:82px;height:82px" role="img" aria-label="Photo of the inside of a coach"></div>
    <div class="photo photo--seats" style="left:62px;top:218px;width:96px;height:96px" role="img" aria-label="Photo of coach seats and aisle"></div>
    <div class="section" style="left:170px;top:30px;width:140px">
      <h2>Weddings &amp; Events</h2>
      <p>Arrive in style on your special day. Our coaches carry guests between ceremony, photos and reception, on time and stress free.</p>
    </div>
    <div class="section" style="left:150px;top:116px;width:130px">
      <h2>Events</h2>
      <p>Concerts, festivals and private functions are easier with a dedicated coach and driver waiting for your group.</p>
    </div>
    <div class="note" style="left:140px;top:186px;width:132px">
      Ask about our package rates for wedding parties and event transfers.
      <strong>Quote requests welcome.</strong>
    </div>
    <div class="photo photo--venue" style="left:340px;top:48px;width:82px;height:82px" role="img" aria-label="Photo of a decorated wedding venue"></div>
    <div class="photo photo--garden" style="left:270px;top:218px;width:118px;height:118px" role="img" aria-label="Photo of a garden with palm trees"></div>
  </article>

  <article class="page inside-right">
    <svg class="bg" viewBox="0 0 480 340" preserveAspectRatio="none" aria-hidden="true">
      <path d="M0 40 C80 10 160 30 250 0 H300 C260 40 250 90 200 130 C140 180 60 160 0 200 Z" fill="var(--blue)"/>
      <path d="M300 0 C260 40 250 90 200 130 C140 180 60 160 0 200" fill="none" stroke="var(--green-light)" stroke-width="5"/>
      <path d="M310 0 C270 44 258 96 208 138 C148 188 64 170 0 210" fill="none" stroke="var(--green)" stroke-width="2"/>
      <path d="M0 210 C70 190 120 250 150 340 H0 Z" fill="var(--blue-pale)"/>
      <path d="M360 340 C390 300 440 280 480 270 V340 Z" fill="var(--blue-light)"/>
    </svg>
    <div class="section section--on-blue" style="left:24px;top:40px;width:150px">
      <h2>Corporate Groups</h2>
      <p>Conferences, staff days and airport transfers handled with professional drivers and clean, air conditioned coaches.</p>
    </div>
    <div class="note" style="left:300px;top:18px;width:166px">
      Every coach is fully accredited, seat belted and maintained to the highest safety standards.
      <strong>School excursions, camps and sports carnivals covered.</strong>
    </div>
    <div class="photo photo--students" style="left:40px;top:180px;width:112px;height:112px" role="img" aria-label="Photo of a school group in uniforms beside a coach"></div>
    <div class="section" style="left:300px;top:100px;width:160px">
      <h2>Educational Groups</h2>
      <p>Safe, reliable transport for excursions and camps, with drivers who hold working with children checks.</p>
    </div>
    <div class="section" style="left:280px;top:178px;width:120px">
      <h2>Sporting Groups</h2>
      <p>Take the whole team to games and tournaments, with room for kit and supporters.</p>
    </div>
    <div class="photo photo--pool" style="left:400px;top:190px;width:66px;height:66px" role="img" aria-label="Photo of a swimming pool lane"></div>
    <div class="photo photo--field" style="left:370px;top:240px;width:90px;height:90px" role="img" aria-label="Photo of a sports field in a stadium"></div>
    <p class="closing" style="left:200px;right:auto;bottom:20px">Call us today for a free quote on <strong>1300 000 482</strong></p>
  </article>
</section>

</body>
</html>
```